Prepared ready to cook meal delivery service needs a flyer design

We need a flyer design for a startup company based in Cape Town, South Africa. I've attached a few flyer designs that I like.

The company is called 'Brindle' and our website will be found at brindle.co.za. We don't have a logo yet.

Flyer text:

Brindle
Ready to roast

Do you feel like a home cooked meal but don't like shopping, peeling, chopping, cooking, or cleaning up?

We deliver ready to roast free range chicken and fresh vegetables to your door.

To order: SMS your name to 083 614 2958 and we'll call you back.

Only the best ingredients used
Free range chickens. Fresh herbs and vegetables. Virgin olive oil.

No bad carbs!

Ready to roast Free range chicken and fresh veggies
For 2 R99
For 4 R139
Updates

Wording of flyer updated.

Target Market(s)

Local Cape Townians that hate grocery shopping and need help saving time preparing meals.

Industry/Entity Type

Delivery Service

Requirements
Must have
• To find out more: SMS your name to 083 614 2958

```html
<!DOCTYPE html>
<html lang="en">
<head>
<meta charset="utf-8">
<title>Brindle – Life Made Easier flyer</title>
<link rel="stylesheet" href="https://fonts.googleapis.com/css2?family=Montserrat:ital,wght@0,400;0,600;0,700;0,800;1,800;1,900&display=swap">
<style>
  :root {
    --yellow: #e9c52b;
    --orange: #cf4a24;
    --orange-light: #dc6a3c;
    --white: #ffffff;
    --ink: #1d1d1d;
    --body-ink: #444444;
    --stage: #ebe8e3;
    --photo-light: #f4f1ec;
    --photo-mid: #d9c3a0;
  }
  * { box-sizing: border-box; margin: 0; padding: 0; }
  html, body {
    width: 1200px; height: 1000px; overflow: hidden;
    background: var(--stage);
    font-family: "Montserrat", Arial, sans-serif;
  }
  .flyer {
    position: absolute; left: 300px; top: 40px;
    width: 600px; height: 920px;
    background: var(--white);
    overflow: hidden;
    box-shadow: 0 8px 24px rgba(0,0,0,.18);
  }
  .flyer__shapes { position: absolute; inset: 0; }
  .headline {
    position: absolute; left: 36px; top: 26px;
    font-weight: 900; font-style: italic;
    font-size: 68px; line-height: .92; letter-spacing: -1px;
    text-transform: uppercase;
  }
  .headline__line--white { color: var(--white); display: block; }
  .headline__line--orange { color: var(--orange); display: block; }

  .hero-photo {
    position: absolute; left: 305px; top: 215px;
    width: 270px; height: 560px;
    background: linear-gradient(180deg, var(--photo-light) 0%, var(--photo-mid) 45%, var(--photo-light) 80%);
    border-radius: 120px 120px 0 0;
  }

  .intro { position: absolute; left: 40px; top: 236px; width: 270px; color: var(--ink); }
  .intro__title { font-size: 21px; font-weight: 800; line-height: 1.1; }
  .intro__subtitle { font-size: 13px; font-weight: 700; line-height: 1.25; margin-bottom: 14px; }
  .intro__copy { font-size: 8.5px; line-height: 1.55; color: var(--body-ink); margin-bottom: 12px; width: 250px; }
  .intro__list { list-style: none; font-size: 8.5px; line-height: 1.6; color: var(--body-ink); width: 255px; margin-top: 24px; }
  .intro__list li { position: relative; padding-left: 10px; }
  .intro__list li::before { content: ""; position: absolute; left: 0; top: 5px; width: 4px; height: 4px; border-radius: 50%; background: var(--ink); }

  .brand {
    position: absolute; left: 330px; top: 770px;
    display: flex; align-items: center; gap: 10px;
    color: var(--white); font-size: 34px; font-weight: 700;
  }
  .brand__mark { width: 14px; height: 14px; background: var(--white); }
  .website {
    position: absolute; right: 40px; top: 838px;
    color: var(--yellow); font-size: 16px; font-weight: 800; font-style: italic;
  }
  .contact-strip {
    position: absolute; left: 0; bottom: 0; width: 100%; height: 44px;
    background: var(--yellow);
    padding: 13px 26px;
    color: var(--orange); font-size: 14px; font-weight: 800; font-style: italic;
  }
</style>
</head>
<body>
  <main class="flyer">
    <svg class="flyer__shapes" width="600" height="920" viewBox="0 0 600 920" aria-hidden="true">
      <polygon points="0,0 600,0 600,320 0,205" fill="var(--yellow)"/>
    </svg>

    <div class="hero-photo" role="img" aria-label="Photo of a smiling woman in white holding a paper grocery bag of fresh vegetables"></div>

    <svg class="flyer__shapes" width="600" height="920" viewBox="0 0 600 920" aria-hidden="true">
      <defs>
        <linearGradient id="bandShine" x1="0" y1="0" x2="1" y2="0">
          <stop offset="0" stop-color="var(--orange)"/>
          <stop offset="0.6" stop-color="var(--orange-light)"/>
          <stop offset="1" stop-color="var(--orange)"/>
        </linearGradient>
      </defs>
      <polygon points="0,690 600,760 600,920 0,920" fill="url(#bandShine)"/>
    </svg>

    <h1 class="headline">
      <span class="headline__line--white">Life Made</span>
      <span class="headline__line--orange">Easier</span>
    </h1>

    <section class="intro">
      <h2 class="intro__title">Lorem ipsum dolor sit</h2>
      <p class="intro__subtitle">amet, consectetuer adipiscing elit.</p>
      <p class="intro__copy">Fresh free range chicken and crisp seasonal vegetables, prepared by hand and packed with herbs and virgin olive oil. We peel, chop and season everything so you simply roast and enjoy a home cooked meal without the effort.</p>
      <p class="intro__copy">No shopping, no peeling and no cleaning up. Order by SMS and we deliver to your door anywhere in Cape Town, ready for the oven.</p>
      <ul class="intro__list">
        <li>Only the best ingredients used in every box</li>
        <li>Free range chickens from local farms</li>
        <li>Fresh herbs and vegetables, washed and chopped</li>
        <li>Virgin olive oil and no bad carbs</li>
        <li>Ready to roast for 2 at R99, for 4 at R139</li>
      </ul>
    </section>

    <div class="brand"><span class="brand__mark"></span>Brindle</div>
    <p class="website">www.brindle.co.za</p>
    <p class="contact-strip">To find out more SMS your name to 083 614 2958</p>
  </main>
</body>
</html>
```